Harbor Emberlights - Woodwick candles needing a sylish box designed

We need a box designed for our woodwick candles.
I would like to see a box that looks very stylish and I would like the logo to be in a silver foil outlined box (I will include photos of examples). I like a box that has a silver foil edge around it, though not essential. A pattern of some sort would be nice on the box, staying with the wood/beach theme. I will also need to include other information on the back of the box about the candle (can I do this after I see the design?). I need to be able to change the fragrance when needed on the box label. The box size is L105mm W105mm H128mm. I am really open to any ideas. Looking for something very stylish and luxurious looking.
The lids on my candles are silver and the candles have a wooden wick.

Target Market(s)

Department stores and retail shops

Industry/Entity Type

Retail

Colors
ffffff

Requirements
Must have
• Looking for something very stylish and luxurious looking, that will look and fit great in any large department store.
Nice to have
• Wooden look, if possible.
• Clean and crisp look. Very pretty.

```html
<!DOCTYPE html>
<html lang="en">
<head>
<meta charset="utf-8">
<title>Harbor Emberlights – Candle Box Dieline</title>
<link rel="stylesheet" href="https://fonts.googleapis.com/css2?family=Cinzel:wght@400&display=swap">
<style>
  :root {
    --page-bg: #f2f2f2;
    --wood-dark: #6b3a1c;
    --wood-mid: #8a4f28;
    --wood-light: #a0643a;
    --silver-light: #f1f1f1;
    --silver-mid: #c9c9c9;
    --silver-dark: #9a9a9a;
    --foil-text: #eeeeee;
    --ink: #1b1b1b;
  }
  html, body {
    margin: 0;
    padding: 0;
    overflow: hidden;
  }
  body {
    width: 857px;
    height: 1200px;
    background: var(--page-bg);
    position: relative;
    font-family: "Cinzel", serif;
  }
  .dieline {
    position: absolute;
    left: 0;
    top: 0;
    width: 857px;
    height: 1200px;
  }
  .brand-sign {
    position: absolute;
    left: 38px;
    top: 1128px;
    margin: 0;
    font-family: "Cinzel", serif;
    font-weight: 400;
    font-size: 29px;
    letter-spacing: 1px;
    color: var(--ink);
  }
  .front-name {
    font-family: "Cinzel", serif;
    font-size: 15px;
    fill: var(--foil-text);
    letter-spacing: 0.8px;
  }
  .label-title {
    font-family: "Cinzel", serif;
    font-size: 11px;
    fill: var(--foil-text);
  }
  .label-copy {
    font-family: "Cinzel", serif;
    font-size: 6.5px;
    fill: var(--foil-text);
  }
  .tab-scent {
    font-family: "Cinzel", serif;
    font-size: 11.5px;
    fill: var(--ink);
  }
</style>
</head>
<body>
<svg class="dieline" viewBox="0 0 857 1200" xmlns="http://www.w3.org/2000/svg">
  <defs>
    <linearGradient id="wood" x1="0" y1="0" x2="1" y2="0">
      <stop offset="0" stop-color="#7a4320"/>
      <stop offset="0.3" stop-color="#94552b"/>
      <stop offset="0.55" stop-color="#6f3b1c"/>
      <stop offset="0.8" stop-color="#9a5c31"/>
      <stop offset="1" stop-color="#7d4622"/>
    </linearGradient>
    <linearGradient id="silver" x1="0" y1="0" x2="1" y2="1">
      <stop offset="0" stop-color="#d6d6d6"/>
      <stop offset="0.35" stop-color="#f2f2f2"/>
      <stop offset="0.6" stop-color="#bdbdbd"/>
      <stop offset="1" stop-color="#e4e4e4"/>
    </linearGradient>
    <radialGradient id="silverTab" cx="0.5" cy="0.3" r="0.7">
      <stop offset="0" stop-color="#e8e8e8"/>
      <stop offset="0.35" stop-color="#9e9e9e"/>
      <stop offset="1" stop-color="#d9d9d9"/>
    </radialGradient>
  </defs>

  <!-- bottom closure tab -->
  <polygon class="closure-tab" fill="url(#silverTab)"
    points="298,694 556,694 556,712 638,712 666,890 556,912 556,996 298,928 298,912 260,890 276,712 298,712"/>
  <text class="tab-scent" x="425" y="914" text-anchor="middle">Sage Mint</text>
  <text class="tab-scent" x="425" y="929" text-anchor="middle">Driftwood Haze</text>

  <!-- central silver spine -->
  <rect class="spine" x="298" y="90" width="258" height="604" fill="url(#silver)"/>

  <!-- side flaps silver frames -->
  <rect class="flap-frame" x="81" y="309" width="217" height="181" fill="url(#silver)"/>
  <rect class="flap-frame" x="558" y="309" width="218" height="181" fill="url(#silver)"/>

  <!-- wood panels -->
  <g role="img" aria-label="Walnut wood grain texture">
    <rect x="313" y="102" width="230" height="192" fill="url(#wood)"/>
    <rect x="313" y="322" width="230" height="152" fill="url(#wood)"/>
    <rect x="313" y="502" width="230" height="192" fill="url(#wood)"/>
    <rect x="94" y="322" width="192" height="152" fill="url(#wood)"/>
    <rect x="570" y="322" width="192" height="152" fill="url(#wood)"/>
    <polygon points="104,262 276,262 298,286 298,309 81,309 81,284" fill="url(#wood)"/>
    <polygon points="81,490 298,490 298,512 276,535 104,535 81,512" fill="url(#wood)"/>
    <polygon points="581,262 754,262 776,284 776,309 558,309 558,286" fill="url(#wood)"/>
    <polygon points="558,490 776,490 776,512 754,535 581,535 558,512" fill="url(#wood)"/>
  </g>

  <!-- front panel brand -->
  <circle cx="428" cy="220" r="18" fill="none" stroke="var(--foil-text)" stroke-width="1.5"/>
  <text class="front-name" x="428" y="270" text-anchor="middle">Harbor Emberlights</text>

  <!-- back label, printed upside down -->
  <g class="back-label" transform="rotate(180 428 598)">
    <rect x="331" y="519" width="194" height="158" fill="none" stroke="var(--foil-text)" stroke-width="1"/>
    <rect x="335" y="523" width="186" height="150" fill="none" stroke="var(--foil-text)" stroke-width="0.6"/>
    <text class="label-title" x="428" y="543" text-anchor="middle">Sage Mint</text>
    <text class="label-title" x="428" y="558" text-anchor="middle">Driftwood Haze</text>
    <text class="label-copy" text-anchor="middle">
      <tspan x="428" y="575">Hand poured</tspan>
      <tspan x="428" y="586">soy wax with a crackling</tspan>
      <tspan x="428" y="597">wooden wick for a calm glow</tspan>
      <tspan x="428" y="608">trim wick before each burn</tspan>
      <tspan x="428" y="619">burn for up to three hours</tspan>
      <tspan x="428" y="630">keep away from drafts</tspan>
      <tspan x="428" y="641">never leave burning unattended</tspan>
      <tspan x="428" y="652">keep out of reach of children</tspan>
    </text>
  </g>
</svg>

<p class="brand-sign">Harbor Emberlights</p>
</body>
</html>
```